Design clean technology service-based company website

Hello, We are looking to reskin our company website. We are an environmental inspection company and test for Asbestos, Lead and Mold along with other contaminants. People depend on the results to be accurate and fast. We are regulated by the EPA and State regulations. We work a lot with business to business and business to customer. We are wanting to make our new presentation to be modern and easy for customers to interact with us, understand our process and services while providing valuable environmental informational resource and updates. We are a technology based company and will be providing instantaneous results as reports come in for the customers. We are needing good calls to action on the site to direct them to setup a new inspection. Each user will have a backend access to their job information with invoices, reports, status, etc. We have developed software to be able to proved these reports and want to look the part.

My current website is www.trypelmarix.com

Helllo we are wanting to make sure we have good time to select the right website for us and also have the additional time to select other pages of the website. We have received great designs and have consolidated our requests into a document for the next set of iterations.

Target Market(s)

Home Owners, Contractors, Engineers, Real Estate Agents, Building Owners, Insurance Adjusters

Industry/Entity Type

Environmental Consultant

Number of Pages Required

5+ page

Font styles to use
Sans Serif

Colors
0355a3
9bcb3c
7f7f7f
f5f5f5
000000

Requirements
Must have
• Use our existing logo to design around
• The layouts look good in mobile mode for understanding and selecting services and signing up
• Clean Modern Layout
• Have all pages on the website have a similar layout and feel
• Clearly communicate services along with bundle service packages
• Detail the customer journey with graphic design
• Great call to actions to either schedule inspection online, call, text, chat
Nice to have
• Have an interactive graphic for where to test for lead, asbestos and mold.
• I like the barney kolts top order line bar - see attached
• Have clear question and answer page layouts for asbestos, lead and mold
• Show Company reviews
• Have clear Resources pages for all types of contaminants
Should not have
• My current website is www.trypelmarix.com

```html
<!DOCTYPE html>
<html lang="en">
<head>
<meta charset="utf-8">
<title>Terravane Environmental Inspections</title>
<link href="https://fonts.googleapis.com/css2?family=Oswald:wght@400;500&family=PT+Sans:wght@400;700&display=swap" rel="stylesheet">
<style>
:root{
  --blue:#0355a3;
  --green:#9bcb3c;
  --grey:#7f7f7f;
  --light:#f5f5f5;
  --black:#000000;
  --ink:#222;
  --dark:#1f1f1f;
  --topbar:#3a3a3a;
  --white:#fff;
}
*{box-sizing:border-box;margin:0;padding:0}
html,body{width:1200px;height:3030px;overflow:hidden;background:var(--white)}
body{font-family:"PT Sans",sans-serif;color:var(--ink);position:relative}
.abs{position:absolute}
.heading{font-family:"Oswald",sans-serif;font-weight:400;text-transform:uppercase}
.btn{position:absolute;display:flex;align-items:center;justify-content:center;border-radius:22px;font-family:"Oswald",sans-serif;font-size:12px;text-transform:uppercase;letter-spacing:.3px}
.btn-green{background:var(--green);color:var(--white)}
.btn-blue{background:var(--blue);color:var(--white)}
.btn-white{background:var(--white);color:var(--green)}

/* header */
.site-header{position:absolute;left:0;top:0;width:1200px;height:108px;background:var(--white)}
.brand{position:absolute;left:200px;top:12px;display:flex;align-items:center;gap:8px}
.brand-mark{width:14px;height:14px;background:var(--green)}
.brand-name{font-family:"PT Sans",sans-serif;font-weight:700;font-size:32px;color:var(--green);line-height:1}
.topbar{position:absolute;left:420px;top:0;width:780px;height:68px;background:var(--topbar);clip-path:polygon(18px 0,100% 0,100% 100%,0 100%)}
.contact-pill{position:absolute;top:17px;height:34px;background:var(--green);border-radius:5px;color:var(--white);font-size:12px;font-weight:700;display:flex;align-items:center;gap:10px;padding:0 14px}
.contact-pill span.sep{width:1px;height:20px;background:rgba(255,255,255,.6)}
.search{position:absolute;left:978px;top:26px}
.main-nav{position:absolute;top:80px;left:0;width:1200px;height:20px;font-family:"Oswald",sans-serif;font-size:12.5px;font-weight:500;text-transform:uppercase;color:var(--ink)}
.main-nav a{position:absolute;color:inherit;text-decoration:none}
.main-nav a.active{color:var(--blue)}
.main-nav a.active::after{content:"";position:absolute;left:0;right:0;top:20px;height:2px;background:var(--blue)}

/* hero */
.hero{position:absolute;left:0;top:108px;width:1200px;height:598px}
.hero-photo{position:absolute;inset:0;background:linear-gradient(90deg,#8d8a7e 0%,#b3ad9a 30%,#c7c2b2 55%,#b9b5aa 75%,#9ea3a6 100%)}
.hero-title{position:absolute;left:198px;top:200px;font-family:"Oswald",sans-serif;font-size:38px;line-height:48px;color:var(--black)}
.hero-rule{position:absolute;left:200px;top:306px;width:100px;height:2px;background:var(--black)}
.hero-sub{position:absolute;left:200px;top:336px;font-size:15px;font-weight:700;color:var(--black)}
.slide-arrow{position:absolute;top:302px;width:56px;height:56px;border-radius:50%;background:rgba(30,30,30,.85);display:flex;align-items:center;justify-content:center}

/* service band */
.band{position:absolute;left:0;top:706px;width:1200px;height:106px;background:var(--green);color:var(--white)}
.band-title{position:absolute;left:270px;top:28px;font-family:"Oswald",sans-serif;font-size:22px}
.band-text{position:absolute;left:270px;top:62px;font-size:13px}

/* section heads */
.section-head{position:absolute;left:0;width:1200px;text-align:center}
.section-icon{display:block;margin:0 auto 8px}
.section-head h2{font-family:"Oswald",sans-serif;font-weight:400;font-size:22px;color:var(--black);text-transform:uppercase}
.section-head p{font-family:"Oswald",sans-serif;font-size:10.5px;text-transform:uppercase;color:#444;margin-top:4px}

/* service cards */
.service-card{position:absolute;top:1030px;width:242px;height:112px;background:var(--white);box-shadow:0 3px 8px rgba(0,0,0,.22);text-align:center}
.service-card svg{position:absolute;left:50%;top:12px;transform:translateX(-50%)}
.service-card h3{position:absolute;top:52px;width:100%;font-size:14px;font-weight:700;color:var(--black)}
.service-card p{position:absolute;top:70px;width:100%;font-size:12px;line-height:14px;color:#444;padding:0 40px}
.card-arrow{position:absolute;right:0;bottom:6px;width:26px;height:16px;background:var(--blue);display:flex;align-items:center;justify-content:center}

/* testing */
.testing{position:absolute;left:0;top:1224px;width:1200px;height:514px}
.testing-photo{position:absolute;inset:0;background:linear-gradient(90deg,#d7d9dc 0%,#8d9a86 30%,#6f7d61 60%,#9aa28e 100%)}
.testing-panel{position:absolute;left:200px;top:84px;width:800px;height:292px;background:rgba(30,30,30,.78);color:var(--white);text-align:center}
.testing-panel h2{font-family:"Oswald",sans-serif;font-weight:400;font-size:20px;margin-top:8px}
.testing-panel h4{font-family:"Oswald",sans-serif;font-weight:400;font-size:10.5px;margin-top:6px}
.testing-panel p{font-size:12.5px;line-height:20px;margin:24px 44px 0}

/* testimonials */
.testimonial{position:absolute;top:1946px;width:380px;height:226px;background:var(--white);box-shadow:0 3px 8px rgba(0,0,0,.22)}
.testimonial .portrait{position:absolute;left:0;top:0;width:168px;height:226px;background:linear-gradient(180deg,#e6e6e6,#c9c9c9)}
.testimonial .name-rule{position:absolute;left:156px;top:28px;width:40px;height:2px;background:var(--blue)}
.testimonial h3{position:absolute;left:210px;top:18px;font-size:14px;font-weight:700;color:var(--black)}
.testimonial .date{position:absolute;left:210px;top:46px;font-size:11px;color:#444}
.testimonial p{position:absolute;left:210px;top:74px;width:150px;font-size:12px;line-height:19px;color:#333}
.testimonial .more{position:absolute;left:210px;top:196px;font-size:10.5px;font-weight:700;color:var(--black)}
.pager{position:absolute;top:2202px;width:26px;height:26px;border-radius:50%;background:var(--blue);display:flex;align-items:center;justify-content:center}

/* journey */
.journey-photo{position:absolute;left:200px;top:2262px;width:312px;height:358px;background:linear-gradient(160deg,#8fb2d6 0%,#c7d2d8 45%,#9a9a7a 100%)}
.journey-card{position:absolute;left:510px;top:2300px;width:492px;height:340px;background:linear-gradient(135deg,#ffffff 0%,#f1f1f1 100%);box-shadow:4px 6px 10px rgba(0,0,0,.25)}
.journey-card::before{content:"";position:absolute;left:-6px;top:-6px;width:492px;height:340px;border:1px solid #ccc;background:var(--white);z-index:-1}
.journey-card svg{position:absolute;left:86px;top:20px}
.journey-card h2{position:absolute;left:86px;top:44px;font-family:"Oswald",sans-serif;font-weight:400;font-size:20px;color:var(--black)}
.journey-card h4{position:absolute;left:86px;top:74px;font-family:"Oswald",sans-serif;font-weight:400;font-size:10.5px;color:#222}
.journey-card p{position:absolute;left:86px;top:108px;width:370px;font-size:12.5px;line-height:21px;color:#333}

/* partners */
.partners{position:absolute;left:0;top:2722px;width:1200px;height:104px;background:#efefef}
.badge{position:absolute}

/* footer */
.site-footer{position:absolute;left:0;top:2826px;width:1200px;height:204px;background:var(--dark);color:var(--white);font-size:12px}
.site-footer h5{position:absolute;font-size:12px;font-weight:700;text-transform:uppercase}
.foot-item{position:absolute;display:flex;align-items:center;gap:10px}
.social{position:absolute;top:116px;width:20px;height:20px;border-radius:2px}
.live-chat{position:absolute;left:866px;top:166px;width:136px;height:38px;background:var(--white);border-radius:3px 3px 0 0;display:flex;align-items:center;justify-content:center;gap:10px;color:var(--blue);font-size:13px;font-weight:700}
</style>
</head>
<body>

<header class="site-header">
  <div class="brand"><span class="brand-mark"></span><span class="brand-name">Terravane</span></div>
  <div class="topbar">
    <div class="contact-pill" style="left:34px;width:148px">
      <svg width="14" height="14" viewBox="0 0 24 24"><path d="M6.6 10.8a15 15 0 0 0 6.6 6.6l2.2-2.2c.3-.3.7-.4 1-.2 1.1.4 2.3.6 3.6.6.6 0 1 .4 1 1V20c0 .6-.4 1-1 1A17 17 0 0 1 3 4c0-.6.4-1 1-1h3.5c.6 0 1 .4 1 1 0 1.3.2 2.5.6 3.6.1.3 0 .7-.2 1z" fill="#fff"/></svg>
      <span class="sep"></span><span>CALL :&nbsp; 303-555-0142</span>
    </div>
    <div class="contact-pill" style="left:250px;width:276px">
      <svg width="16" height="14" viewBox="0 0 24 20"><path d="M2 2h20v16H2z" fill="none" stroke="#fff" stroke-width="2"/><path d="M2 3l10 8 10-8" fill="none" stroke="#fff" stroke-width="2"/></svg>
      <span class="sep"></span><span>EMAIL :&nbsp; info@trypelmarix.com</span>
    </div>
    <svg class="search" width="14" height="14" viewBox="0 0 24 24"><circle cx="10" cy="10" r="7" fill="none" stroke="#fff" stroke-width="2.5"/><path d="M15 15l7 7" stroke="#fff" stroke-width="2.5"/></svg>
  </div>
  <nav class="main-nav">
    <a class="active" style="left:236px">Home</a>
    <a style="left:320px">Our Services</a>
    <a style="left:462px">Resources</a>
    <a style="left:586px">Blog</a>
    <a style="left:674px">Q &amp; A</a>
    <a style="left:768px">Reviews</a>
    <a style="left:880px">Connect</a>
  </nav>
</header>

<section class="hero">
  <div class="hero-photo" role="img" aria-label="Smiling inspector in a hard hat and red jacket holding a clipboard at a construction site"></div>
  <h1 class="hero-title">Fast, Dependable Results&nbsp; When It<br>Matters The Most</h1>
  <div class="hero-rule"></div>
  <p class="hero-sub">Asbestos, Mold, Lead&nbsp; inspections</p>
  <a class="btn btn-green" style="left:200px;top:394px;width:122px;height:38px">Learn More</a>
  <a class="btn btn-blue" style="left:334px;top:394px;width:126px;height:38px">Contact Us</a>
  <div class="slide-arrow" style="left:92px"><svg width="18" height="14" viewBox="0 0 18 14"><path d="M17 7H2M7 1L1 7l6 6" fill="none" stroke="#fff" stroke-width="2.2"/></svg></div>
  <div class="slide-arrow" style="left:1048px"><svg width="18" height="14" viewBox="0 0 18 14"><path d="M1 7h15M11 1l6 6-6 6" fill="none" stroke="#fff" stroke-width="2.2"/></svg></div>
</section>

<section class="band">
  <div class="band-title">24/7/365 Same Day Service</div>
  <div class="band-text">Terravane grew up in the rough and tumble disaster restoration industry.</div>
  <a class="btn btn-white" style="left:798px;top:34px;width:126px;height:38px">Contact Us</a>
</section>

<div class="section-head" style="top:878px">
  <svg class="section-icon" width="20" height="20" viewBox="0 0 20 20"><rect x="2" y="5" width="14" height="9" fill="var(--green)"/><circle cx="6" cy="17" r="2" fill="var(--green)"/><circle cx="13" cy="17" r="2" fill="var(--green)"/><path d="M16 5l3-3" stroke="var(--green)" stroke-width="2"/></svg>
  <h2>Our Services</h2>
  <p>We are experienced in assessing the environmental hazards</p>
</div>

<article class="service-card" style="left:200px">
  <svg width="28" height="28" viewBox="0 0 28 28"><circle cx="14" cy="14" r="11" fill="none" stroke="#222" stroke-width="2"/><path d="M6 6l16 16" stroke="#222" stroke-width="2"/><rect x="9" y="12" width="10" height="4" fill="#222"/></svg>
  <h3>Asbestos Inspections</h3>
  <p>Asbestos is a federally regulated .....</p>
  <span class="card-arrow"><svg width="12" height="8" viewBox="0 0 12 8"><path d="M0 4h10M7 1l3 3-3 3" fill="none" stroke="#fff" stroke-width="1.5"/></svg></span>
</article>
<article class="service-card" style="left:480px">
  <svg width="28" height="28" viewBox="0 0 28 28"><path d="M3 14L14 4l11 10" fill="none" stroke="#222" stroke-width="2.2"/><path d="M7 12v12h14V12" fill="#222"/><circle cx="14" cy="18" r="3" fill="#fff"/></svg>
  <h3>Mold Inspections</h3>
  <p>Mold can threaten your family risks.....</p>
  <span class="card-arrow"><svg width="12" height="8" viewBox="0 0 12 8"><path d="M0 4h10M7 1l3 3-3 3" fill="none" stroke="#fff" stroke-width="1.5"/></svg></span>
</article>
<article class="service-card" style="left:760px">
  <svg width="32" height="28" viewBox="0 0 32 28"><path d="M2 16L14 6l12 10" fill="#222"/><rect x="6" y="15" width="16" height="9" fill="#222"/><rect x="20" y="18" width="10" height="6" fill="#222"/></svg>
  <h3>Lead Inspections</h3>
  <p style="color:#777">Lead Exposure Is Unac-ceptable Family</p>
  <span class="card-arrow"><svg width="12" height="8" viewBox="0 0 12 8"><path d="M0 4h10M7 1l3 3-3 3" fill="none" stroke="#fff" stroke-width="1.5"/></svg></span>
</article>

<section class="testing">
  <div class="testing-photo" role="img" aria-label="Engineer in a white hard hat reviewing plans outdoors"></div>
  <div class="testing-panel">
    <svg style="margin-top:26px" width="20" height="20" viewBox="0 0 20 20"><rect x="2" y="5" width="14" height="9" fill="#fff"/><circle cx="6" cy="17" r="2" fill="#fff"/><circle cx="13" cy="17" r="2" fill="#fff"/><path d="M16 5l3-3" stroke="#fff" stroke-width="2"/></svg>
    <h2>ENVIRONMENTAL TESTING EVOLVED</h2>
    <h4>TERRAVANE GREW UP IN THE ROUGH AND TUMBLE DISASTER RESTORATION INDUSTRY</h4>
    <p>Terravane grew up in the rough and tumble disaster restoration industry. Time and time again, we saw projects small and large brought to a stand-still to await environmental testing and results.First, we had to know when it's prudent or even required by law to test for asbestos, lead-based paint, mold or other contaminants.</p>
    <a class="btn btn-white" style="left:338px;top:236px;width:124px;height:38px">Learn More</a>
  </div>
</section>

<div class="section-head" style="top:1808px">
  <svg class="section-icon" width="20" height="20" viewBox="0 0 20 20"><rect x="2" y="5" width="14" height="9" fill="var(--green)"/><circle cx="6" cy="17" r="2" fill="var(--green)"/><circle cx="13" cy="17" r="2" fill="var(--green)"/><path d="M16 5l3-3" stroke="var(--green)" stroke-width="2"/></svg>
  <h2>Our Testimonial</h2>
  <p>We are experienced in assessing the environmental hazards</p>
</div>

<article class="testimonial" style="left:200px">
  <div class="portrait" role="img" aria-label="Portrait of a smiling customer in a grey blazer"></div>
  <span class="name-rule"></span>
  <h3>Dana Whitlow</h3>
  <div class="date">29 Dec-17</div>
  <p>Lorem Ipsum is simply-dummy text of theprint-ing and typesetting industry. Lorem Ipsum has been the industry's standar..</p>
  <div class="more">READ MORE &#10230;</div>
</article>
<article class="testimonial" style="left:620px">
  <div class="portrait" role="img" aria-label="Portrait of a customer in a grey shirt with arms crossed"></div>
  <span class="name-rule"></span>
  <h3>Colin R.</h3>
  <div class="date">29 Dec-17</div>
  <p>Lorem Ipsum is simply-dummy text of theprint-ing and typesetting industry. Lorem Ipsum has been the industry's standar..</p>
  <div class="more">READ MORE &#10230;</div>
</article>
<span class="pager" style="left:568px"><svg width="8" height="10" viewBox="0 0 8 10"><path d="M6 1L2 5l4 4" fill="none" stroke="#fff" stroke-width="2"/></svg></span>
<span class="pager" style="left:604px"><svg width="8" height="10" viewBox="0 0 8 10"><path d="M2 1l4 4-4 4" fill="none" stroke="#fff" stroke-width="2"/></svg></span>

<div class="journey-photo" role="img" aria-label="Two workers in hard hats and safety vests in front of high-rise buildings under construction"></div>
<article class="journey-card">
  <svg width="20" height="20" viewBox="0 0 20 20"><rect x="2" y="5" width="14" height="9" fill="var(--green)"/><circle cx="6" cy="17" r="2" fill="var(--green)"/><circle cx="13" cy="17" r="2" fill="var(--green)"/><path d="M16 5l3-3" stroke="var(--green)" stroke-width="2"/></svg>
  <h2>CUSTOMER JOURNEY</h2>
  <h4>TERRAVANE WERE INCREDIBLY HELPFUL IN OUR HOME BUYINGPROCESS</h4>
  <p>Lorem Ipsum is simply dummy text of the printing and type-setting industry. Lorem Ipsum has been the industry's standard dummy text ever since the 1500s, when an unknown printer took a galley of type and scrambled it to make a type specimen book. It hassurvived..</p>
  <a class="btn btn-green" style="left:86px;top:262px;width:124px;height:38px">Learn More</a>
</article>

<section class="partners">
  <div class="badge" style="left:236px;top:28px;width:136px;height:54px;background:#1e4f72;border-radius:3px"></div>
  <div class="badge" style="left:404px;top:30px;width:140px;height:50px;background:#2b6aa8;border-radius:25px 4px 4px 25px"></div>
  <div class="badge" style="left:566px;top:24px;width:62px;height:62px;background:#5fb7b8;border-radius:50%"></div>
  <div class="badge" style="left:636px;top:40px;width:112px;height:30px;background:#9ab3c4;border-radius:3px"></div>
  <div class="badge" style="left:766px;top:24px;width:56px;height:56px;background:#2f8a3e;clip-path:polygon(50% 0,100% 100%,0 100%)"></div>
  <div class="badge" style="left:834px;top:30px;width:132px;height:48px;background:#6f7a86;border-radius:3px"></div>
</section>

<footer class="site-footer">
  <div class="abs" style="left:200px;top:30px;line-height:20px">&copy;&nbsp; Terravane Environmental<br>Inspections 2017</div>
  <span class="social" style="left:200px;background:#3b5b98"></span>
  <span class="social" style="left:226px;background:#c8232c"></span>
  <span class="social" style="left:252px;background:#2aa3ef"></span>
  <span class="social" style="left:278px;background:#d34836"></span>

  <div class="foot-item" style="left:404px;top:26px"><svg width="16" height="14" viewBox="0 0 16 14"><rect x="1" y="3" width="14" height="10" fill="#ddd"/><rect x="4" y="0" width="8" height="4" fill="#ddd"/></svg>Commercial Service</div>
  <div class="foot-item" style="left:404px;top:56px"><svg width="16" height="14" viewBox="0 0 16 14"><path d="M1 7L8 1l7 6v7H1z" fill="#ddd"/></svg>Residential Service</div>
  <div class="foot-item" style="left:404px;top:86px"><svg width="16" height="14" viewBox="0 0 16 14"><path d="M1 7L8 1l7 6" fill="none" stroke="#ddd" stroke-width="2"/><rect x="4" y="7" width="8" height="7" fill="#ddd"/></svg>Homeowner Service</div>
  <div class="foot-item" style="left:404px;top:116px"><svg width="16" height="14" viewBox="0 0 16 14"><circle cx="8" cy="4" r="3" fill="#ddd"/><path d="M2 14c0-4 3-6 6-6s6 2 6 6z" fill="#ddd"/></svg>Contracter Service</div>

  <h5 style="left:596px;top:26px">Keep In Touch</h5>
  <div class="foot-item" style="left:598px;top:56px"><svg width="10" height="16" viewBox="0 0 10 16"><rect x="1" y="1" width="8" height="14" rx="1.5" fill="none" stroke="#fff" stroke-width="1.5"/></svg>303-555-0142</div>
  <div class="foot-item" style="left:596px;top:86px"><svg width="14" height="12" viewBox="0 0 14 12"><path d="M1 1h12v10H1z" fill="none" stroke="#fff" stroke-width="1.3"/><path d="M1 2l6 5 6-5" fill="none" stroke="#fff" stroke-width="1.3"/></svg>info@trypelmarix.com</div>

  <h5 style="left:814px;top:26px">Address</h5>
  <div class="foot-item" style="left:814px;top:58px;align-items:flex-start"><svg width="16" height="14" viewBox="0 0 16 14"><path d="M1 7L8 1l7 6v7H1z" fill="#fff"/></svg><span style="line-height:20px">2240 W. Alder Ave. Ste.<br>B12 Denver, Co. 80219</span></div>

  <div class="live-chat"><svg width="22" height="18" viewBox="0 0 22 18"><path d="M2 2h12v8H6l-4 3z" fill="none" stroke="var(--green)" stroke-width="1.8"/><path d="M16 6h4v8l-3-2h-7v-2" fill="none" stroke="var(--green)" stroke-width="1.8"/></svg>Live Chat</div>
</footer>

</body>
</html>
```